Brindmoor Packaging Design

Influenced by the Ivy League look, Brindmoor is a classic shirt manufacturer based in London, England. The shirts are made from the highest quality cottons and materials. Manufactured in England, utilising expert craftsmanship to design and manufacture this premium product. It is likely to be worn by men for business and special occasions. The look is not fashion dictated but a classic reliable brand that will over time have advocates of the shirts. We are looking for a high quality classic packaging design that is adds to the customer experience.
Updates
Project Deadline Extended
Reason: No suitable designs received to date. We are looking for a fully packaging design which also includes the swing label and for example collar packaging
Target Market(s)
Likely to be worn by men for business and special occasions. Who are aware of classic styling
Industry/Entity Type
Business
Font styles to use
Other font styles liked:
- avenvir
Look and feel
Each slider illustrates characteristics of the customer's brand and the style your logo design should communicate.

```html
<!DOCTYPE html>
<html lang="en">
<head>
<meta charset="utf-8">
<title>Brindmoor Packaging Design – Outer Shell</title>
<link rel="stylesheet" href="https://fonts.googleapis.com/css2?family=Montserrat:wght@500&family=Noto+Sans:wght@400&display=swap">
<style>
  :root {
    --page: #ffffff;
    --frame: #000000;
    --banner: #2a2a2a;
    --shell: #1e201f;
    --gold: #d8bd70;
    --gold-line: #7a6a3a;
    --label: #555555;
    --white: #ffffff;
  }
  * { box-sizing: border-box; margin: 0; padding: 0; }
  html, body { width: 1200px; height: 1000px; overflow: hidden; background: var(--page); }
  .sheet { position: relative; width: 1200px; height: 1000px; }
  .sheet-frame {
    position: absolute; left: 23px; top: 18px; width: 1154px; height: 962px;
    border: 3px solid var(--frame);
  }
  .brand-banner { position: absolute; left: 51px; top: 18px; width: 295px; height: 188px; }
  .banner-shape { position: absolute; inset: 0; }
  .banner-mark {
    position: absolute; left: 111px; top: 24px; width: 72px; height: 72px;
    border: 5px solid var(--white); border-radius: 50%;
  }
  .banner-name {
    position: absolute; left: 0; width: 295px; top: 114px; text-align: center;
    font-family: "Montserrat", sans-serif; font-weight: 500; font-size: 28px;
    letter-spacing: 4px; color: var(--white);
  }
  .sheet-title {
    position: absolute; left: 560px; width: 400px; top: 90px; text-align: center;
    font-family: "Noto Sans", sans-serif; font-weight: 400; font-size: 34px;
    color: var(--label); text-decoration: underline; text-decoration-thickness: 2px;
    text-underline-offset: 5px;
  }
  .panel { position: absolute; background: var(--shell); }
  .panel-inner { position: absolute; border: 1px solid var(--gold-line); }
  .panel-label {
    position: absolute; top: 856px; width: 200px; text-align: center;
    font-family: "Noto Sans", sans-serif; font-size: 17px; color: var(--label);
  }
  .gold-mark { position: absolute; border-radius: 50%; border: 3px solid var(--gold); }
  .gold-name {
    position: absolute; font-family: "Montserrat", sans-serif; font-weight: 500;
    color: var(--gold); white-space: nowrap;
  }
  .panel-front { left: 86px; top: 310px; width: 425px; height: 539px; }
  .panel-side { left: 549px; top: 311px; width: 99px; height: 537px; }
  .panel-back { left: 687px; top: 311px; width: 424px; height: 537px; }
</style>
</head>
<body>
<main class="sheet">
  <div class="sheet-frame"></div>

  <header class="brand-banner">
    <svg class="banner-shape" width="295" height="188" viewBox="0 0 295 188" aria-hidden="true">
      <path d="M0 0 H295 V186 Q147 178 0 186 Z" fill="var(--banner)"/>
    </svg>
    <div class="banner-mark"></div>
    <div class="banner-name">BRINDMOOR</div>
  </header>

  <h1 class="sheet-title">Outer Shell Design</h1>

  <section class="panel panel-front">
    <div class="panel-inner" style="left:10px; top:12px; width:405px; height:514px;"></div>
    <div class="gold-mark" style="left:179px; top:207px; width:66px; height:66px;"></div>
    <div class="gold-name" style="left:0; width:425px; text-align:center; top:289px; font-size:27px; letter-spacing:4px;">BRINDMOOR</div>
  </section>
  <div class="panel-label" style="left:198px;">Front</div>

  <section class="panel panel-side">
    <div class="gold-mark" style="left:29px; top:477px; width:42px; height:42px;"></div>
  </section>
  <div class="panel-label" style="left:498px;">Side</div>

  <section class="panel panel-back">
    <div class="panel-inner" style="left:10px; top:12px; width:404px; height:512px;"></div>
    <div class="gold-mark" style="left:142px; top:467px; width:36px; height:36px;"></div>
    <div class="gold-name" style="left:184px; top:475px; font-size:17px; letter-spacing:2.5px;">BRINDMOOR</div>
  </section>
  <div class="panel-label" style="left:799px;">Back</div>
</main>
</body>
</html>
```